Business Card Ayurvedic Massage

I'm starting with my ayurvedic massage business and need a business card design. The design should be inline with my brand/logo as well as with the design of my website (www.mirelo-dant.ch).
Front: logo and text "Ayurvedische Massagen"
back: name and adress (see details https://www.mirelo-dant.ch/kontakt.html)

```html
<!DOCTYPE html>
<html lang="de">
<head>
<meta charset="utf-8">
<title>mirelo-dant – Visitenkarte</title>
<link href="https://fonts.googleapis.com/css2?family=Oswald:wght@600&family=Roboto:wght@400&display=swap" rel="stylesheet">
<style>
  :root {
    --maroon: #6b0d1e;
    --maroon-dark: #560a17;
    --gold: #c8901f;
    --gold-light: #e2b24a;
    --paper: #ffffff;
    --ink: #2b2b2b;
    --stage: #ecebe8;
  }
  * { margin: 0; padding: 0; box-sizing: border-box; }
  html, body { width: 1200px; height: 900px; overflow: hidden; }
  body { background: var(--stage); position: relative; font-family: "Roboto", Arial, sans-serif; }

  .card {
    position: absolute; left: 250px; width: 700px; height: 400px;
    background: var(--maroon); overflow: hidden;
    box-shadow: 0 6px 18px rgba(0,0,0,.18);
  }
  .card-back { top: 30px; }
  .card-front { top: 470px; }
  .card-shape { position: absolute; inset: 0; width: 100%; height: 100%; }

  .elephant-art {
    position: absolute;
    background: linear-gradient(160deg, var(--gold-light), var(--gold) 45%, var(--maroon) 100%);
    border-radius: 10px;
  }
  .brand-name {
    position: absolute; font-family: "Oswald", Impact, sans-serif; font-weight: 600;
    color: var(--gold); letter-spacing: 1px; white-space: nowrap;
  }
  .tagline {
    position: absolute; font-family: "Oswald", Impact, sans-serif; font-weight: 600;
    color: var(--gold); letter-spacing: 1px; white-space: nowrap; text-transform: uppercase;
  }

  /* front */
  .card-front .elephant-left  { left: 192px; top: 108px; width: 88px; height: 110px; }
  .card-front .elephant-right { left: 478px; top: 136px; width: 88px; height: 110px; }
  .card-front .brand-name { left: 288px; top: 158px; font-size: 26px; line-height: 1.2; }
  .card-front .tagline { left: 222px; top: 258px; font-size: 30px; line-height: 1.2; }

  /* back */
  .card-back .elephant-left  { left: 70px; top: 100px; width: 58px; height: 72px; }
  .card-back .elephant-right { left: 232px; top: 82px; width: 58px; height: 72px; }
  .card-back .brand-name { left: 132px; top: 112px; font-size: 18px; }
  .card-back .tagline { left: 378px; top: 92px; font-size: 22px; }

  .contact-list { position: absolute; left: 378px; top: 150px; list-style: none; }
  .contact-item {
    display: flex; align-items: flex-start; gap: 10px; margin-bottom: 9px;
    font-size: 12px; line-height: 1.3; color: var(--ink); font-variant: small-caps;
  }
  .contact-icon {
    flex: 0 0 18px; width: 18px; height: 18px; border: 1.5px solid var(--gold);
    border-radius: 50%; display: flex; align-items: center; justify-content: center;
  }
  .contact-icon svg { width: 10px; height: 10px; }
</style>
</head>
<body>

<section class="card card-back" aria-label="Rückseite">
  <svg class="card-shape" viewBox="0 0 700 400" aria-hidden="true">
    <path d="M20,0 L580,0 C630,30 665,70 700,120 L700,300 C600,285 500,300 400,322 C290,346 200,332 150,352 C120,300 125,240 75,205 C35,175 40,90 20,0 Z" fill="var(--gold)" transform="translate(0,6)"/>
    <path d="M20,0 L580,0 C630,30 665,70 700,120 L700,300 C600,285 500,300 400,322 C290,346 200,332 150,352 C120,300 125,240 75,205 C35,175 40,90 20,0 Z" fill="var(--paper)"/>
  </svg>
  <div class="elephant-art elephant-left" role="img" aria-label="Geschmückter Elefant mit Schirm"></div>
  <span class="brand-name">mirelo-dant</span>
  <div class="elephant-art elephant-right" role="img" aria-label="Geschmückter Elefant mit Schirm"></div>
  <h2 class="tagline">Ayurvedische Massagen</h2>
  <ul class="contact-list">
    <li class="contact-item">
      <span class="contact-icon"><svg viewBox="0 0 10 10"><path d="M5 1a3 3 0 0 0-3 3c0 2 3 5 3 5s3-3 3-5a3 3 0 0 0-3-3z" fill="var(--gold)"/></svg></span>
      <span>Lena Vorburg, mirelo-dant,<br>Talackerweg 5, 8852 Altendorf (SZ)</span>
    </li>
    <li class="contact-item">
      <span class="contact-icon"><svg viewBox="0 0 10 10"><rect x="1" y="2.5" width="8" height="5" fill="var(--gold)"/><path d="M1 2.5 5 5.5 9 2.5" stroke="#fff" fill="none" stroke-width=".8"/></svg></span>
      <span>info@mirelo-dant.ch</span>
    </li>
    <li class="contact-item">
      <span class="contact-icon"><svg viewBox="0 0 10 10"><path d="M2 1.5 3.5 1 4.5 3.5 3.5 4.3C4 5.5 4.7 6.2 5.8 6.6L6.6 5.6 9 6.5 8.5 8C5 8.5 1.5 5 2 1.5Z" fill="var(--gold)"/></svg></span>
      <span>+41 77 000 12 34 (Bitte keine Werbung)</span>
    </li>
    <li class="contact-item">
      <span class="contact-icon"><svg viewBox="0 0 10 10"><circle cx="5" cy="5" r="3.5" stroke="var(--gold)" fill="none"/><path d="M1.5 5h7M5 1.5v7" stroke="var(--gold)" stroke-width=".8"/></svg></span>
      <span>www.mirelo-dant.ch</span>
    </li>
  </ul>
</section>

<section class="card card-front" aria-label="Vorderseite">
  <svg class="card-shape" viewBox="0 0 700 400" aria-hidden="true">
    <path d="M70,30 C200,20 330,80 470,100 C580,115 650,92 700,82 L700,215 C660,240 660,300 700,330 L700,345 C560,330 460,350 360,400 L50,400 C90,330 100,250 60,180 C40,130 40,50 70,30 Z" fill="var(--gold)" transform="translate(-4,-6)"/>
    <path d="M70,30 C200,20 330,80 470,100 C580,115 650,92 700,82 L700,215 C660,240 660,300 700,330 L700,345 C560,330 460,350 360,400 L50,400 C90,330 100,250 60,180 C40,130 40,50 70,30 Z" fill="var(--paper)"/>
  </svg>
  <div class="elephant-art elephant-left" role="img" aria-label="Geschmückter Elefant mit Schirm"></div>
  <span class="brand-name">mirelo-dant</span>
  <div class="elephant-art elephant-right" role="img" aria-label="Geschmückter Elefant mit Schirm"></div>
  <h1 class="tagline">Ayurvedische Massagen</h1>
</section>

</body>
</html>
```